Book Cover Design Project - SIMPLE ART, Pre-Concepted

We already have a full design concept for the cover art. It is however in a low quality word document format. This project is to recreate existing example guideline art in as much vector art possible for great quality print production. Artistic flare is welcome. This will be for a book cover (front/back) and I want the quality to be excellent.

Art to be provided in Adobe Illustrator format. The book will be 6wide x 9high, so the artboard for the cover needs to be set up to 12.5 wide x 9 high with .125" bleeds.

Copy content for the spine: "Beneath the Orchard Lamps at Dusk" RL Ombrisko.

Here is a link to download the word document "template" and a new photo for the back page. I'm not sure that I like the new photo, it is possible the old one in the word document will work.

www.kelmarpressworks.com/uploads/BriefingFilesSetAll.zip

I've got a fast deadline on this project because the client would like to have manufacturing completed by Christmas...which is why this is only a 2 day project. I appreciate your interest in our project.

Gordon

Try this link...seems I was missing the .zip extension which may have been causing problems.

Requirements
Must have
• Adobe Illustrator Files
CMYK color setup - no color definitions for project
Artboard Size: 12.625 wide x 9.125 high
Art Orientation: Flat image should have the back book page on the left side, front page on the right side, spine copy running down the middle.

```html
<!DOCTYPE html>
<html lang="en">
<head>
<meta charset="utf-8">
<title>Beneath the Orchard Lamps at Dusk — Cover Spread</title>
<link rel="stylesheet" href="https://fonts.googleapis.com/css2?family=Arimo:wght@400;700&family=Nunito:ital,wght@0,900;1,800&display=swap">
<style>
  :root {
    --purple-deep: #4a3f8a;
    --purple-band: #5a4f98;
    --title-ink: #3b2f7a;
    --spine-blue: #1f6fb8;
    --coral: #f08a6e;
    --orange: #f29a4a;
    --blush: #f7d2d6;
    --sea: #8f8fb0;
    --white: #ffffff;
    --body-ink: #111111;
    --panel: rgba(255, 255, 255, 0.55);
  }
  * { box-sizing: border-box; margin: 0; padding: 0; }
  html, body { width: 1200px; height: 780px; overflow: hidden; background: #fff; }
  .spread {
    position: relative; width: 1200px; height: 780px; overflow: hidden;
    font-family: "Arimo", Arial, sans-serif;
  }
  .artwork { position: absolute; inset: 0; }

  /* back cover */
  .author-photo {
    position: absolute; left: 0; top: 0; width: 262px; height: 292px;
    background: linear-gradient(160deg, #b9b4b6 0%, #6d625f 45%, #2f2a29 100%);
    z-index: 2;
  }
  .bio-panel {
    position: absolute; left: 0; top: 20px; width: 425px; height: 678px;
    background: var(--panel);
    padding: 0 4px 0 6px;
    color: var(--body-ink); font-size: 10.4px; line-height: 12.35px;
  }
  .bio-panel .photo-space { float: left; width: 262px; height: 272px; margin-right: 4px; shape-outside: inset(0); }
  .bio-panel p { margin: 0; }
  .drop-cap { float: left; font-size: 36px; line-height: 30px; margin: 2px 3px 0 0; }

  /* spine */
  .spine {
    position: absolute; left: 580px; top: 0; width: 36px; height: 780px;
    background: rgba(255, 255, 255, 0.35);
  }
  .spine-text {
    position: absolute; left: 50%; transform: translateX(-50%) rotate(90deg);
    transform-origin: center; white-space: nowrap;
    color: var(--spine-blue); font-weight: 700; font-size: 13px; letter-spacing: 0.2px;
  }
  .spine-author { top: 232px; }
  .spine-series { top: 505px; font-size: 14px; }

  /* front cover */
  .publisher-bar {
    position: absolute; left: 914px; top: 0; width: 286px; height: 44px;
    background: linear-gradient(90deg, rgba(90,79,152,0) 0%, var(--purple-band) 22%, var(--purple-deep) 100%);
    color: var(--white); font-family: "Nunito", sans-serif; font-style: italic; font-weight: 800;
    font-size: 27px; line-height: 44px; text-align: right; padding-right: 18px;
  }
  .book-title {
    position: absolute; left: 622px; top: 66px; width: 578px; text-align: center;
    font-family: "Nunito", sans-serif; font-weight: 900; font-size: 60px; line-height: 72px;
    color: var(--title-ink); letter-spacing: 0.5px;
    -webkit-text-stroke: 1px #fff;
    text-shadow: 2px 2px 0 #fff, -2px -2px 0 #fff, 2px -2px 0 #fff, -2px 2px 0 #fff, 4px 4px 4px rgba(80,60,120,.55);
  }
  .front-footer { position: absolute; left: 622px; top: 700px; width: 578px; height: 80px; }
  .front-footer-text {
    position: absolute; left: 0; right: 0; bottom: 14px; text-align: center;
    color: var(--white); font-weight: 700; font-size: 13px; letter-spacing: 0.4px;
  }
</style>
</head>
<body>
<main class="spread">
  <svg class="artwork" width="1200" height="780" viewBox="0 0 1200 780" role="img" aria-label="Abstract background of swirling coral, orange and white light with sweeping arrow shapes over a soft violet sea">
    <defs>
      <linearGradient id="backWash" x1="0" y1="0" x2="0" y2="1">
        <stop offset="0" stop-color="#e7c7d6"/>
        <stop offset="0.55" stop-color="#d7a7bf"/>
        <stop offset="1" stop-color="var(--sea)"/>
      </linearGradient>
      <radialGradient id="frontGlow" cx="0.62" cy="0.48" r="0.7">
        <stop offset="0" stop-color="#ffffff"/>
        <stop offset="0.35" stop-color="#fbe3e6"/>
        <stop offset="0.7" stop-color="#f3a594"/>
        <stop offset="1" stop-color="#f4c2c8"/>
      </radialGradient>
      <linearGradient id="streak" x1="0" y1="0" x2="1" y2="1">
        <stop offset="0" stop-color="#f6b08a" stop-opacity="0.2"/>
        <stop offset="0.5" stop-color="#f08a4e" stop-opacity="0.85"/>
        <stop offset="1" stop-color="#f6b08a" stop-opacity="0.3"/>
      </linearGradient>
    </defs>
    <rect width="600" height="780" fill="url(#backWash)"/>
    <rect x="400" width="800" height="780" fill="url(#frontGlow)"/>
    <path d="M380 150 L520 120 L1200 700 L1200 780 L1110 780 Z" fill="url(#streak)"/>
  </svg>

  <section class="back-cover">
    <div class="author-photo" role="img" aria-label="Portrait photograph of the author"></div>
    <div class="bio-panel">
      <div class="photo-space"></div>
      <p><span class="drop-cap">A</span>bout the author: The word of God says that “I know the plans I have for you” (Jeremiah 29:11) and that “before I formed you in the womb I knew you” (Jeremiah 1:15). These verses of scripture depict the life of Rowan L Ombrisko.</p>
      <p>As a little boy Rowan was always told that he was going to be a preacher. The magnitude of this repeated statement and exactly what it entailed was not taken seriously or truly understood, at that time. It was not Rowan’s plan or desire to be a preacher, and he tried to do anything and everything to avoid the talks of him becoming one. Rowan’s path of life, although he believed in God, took him down the road that led him away from God. His struggles with life’s events and being an introvert kept him emotionally troubled, in a state of depression and wanting to commit suicide. Yet, as the Lord was with Jeremiah, even so was the Lord with Rowan. The Lord was to show Rowan just what it meant to have complete trust in Him and to know that He would always provide a way of an escape. Before Rowan came to the point of carrying out his plans to commit suicide, he prayed a simple prayer that God would give him a new family. At that exact moment Rowan’s life began to take a new direction. He began to seek after the Lord; it became his quest to find out what it meant to be a servant of God. Because of his being an introvert, he began to write his emotions on paper in the form of poems. Those poems gave him the strength to come out of depression and began his two year journey to find God.</p>
      <p>Rowan’s relationship with Jesus and salvation journey began at the age of nineteen. The poetry writing started as a therapeutic remedy for his troubled past, but developed into the psalms of Rowan because of God’s grace and mercy that delivered him from despair and hopelessness.</p>
      <p>God’s favor covers Rowan’s life and carries him from day to day. It is written that “without me (Christ) ye can do nothing” (John 15:5). This scripture resonates in Rowan’s heart. For, he truly believes that God is the author and he is just the vessel used of God. His desire is that each poem will be taken personally and become a tool used by everyone to help them on their Christian journey and to let them know that they are never alone in their experience and quest to be closer to the Lord Jesus Christ.</p>
    </div>
  </section>

  <section class="spine">
    <span class="spine-text spine-author">by RL Ombrisko</span>
    <span class="spine-text spine-series">A compilation of poems</span>
  </section>

  <section class="front-cover">
    <div class="publisher-bar">Pubisher’s Name</div>
    <h1 class="book-title">Beneath the<br>Orchard Lamps<br>at Dusk</h1>
    <div class="front-footer">
      <svg width="578" height="80" viewBox="0 0 578 80" aria-hidden="true">
        <path d="M0 22 Q300 32 578 0 L578 80 L0 80 Z" fill="var(--purple-band)"/>
        <path d="M0 22 Q300 32 578 0" fill="none" stroke="#fff" stroke-width="3"/>
      </svg>
      <p class="front-footer-text">A compilation of poems by RL Ombrisko</p>
    </div>
  </section>
</main>
</body>
</html>
```